Fresh, modern brand required for new start-up!

TallCedarRun is a new venture offering an end-to-end communications and media relations service including strategy development, execution and evaluation; copy writing and editing; social and e- media management; leadership coaching, media training and more.

I require a fresh and lively corporate identity to mirror the ethos of the business.

I need a logo, business card (double-sided preferably), letterhead (for invoicing and client communications) and compliment slip. As a start-up, budget will be an ongoing consideration for me so, ideally, I would prefer a two-colour logo - although if you wow me with something more than that, I may have to throw caution to the wind!

The ethos behind my name is twofold; one, I have moved from being something of a "big fish in a small pond" (a director in a single company) to a small fish in the big pond of small businesses. Two, I may be a "small fish", but that doesn't mean I don't "fish big".

I am looking for a clean, simple design that will look good on a variety of mediums, big or small. The design should be young and fresh and make an immediate impact. I want the design to reflect the fact that I specialise in tailored, simple and effective communications.

Target Market(s)

My clients range from global financial services, resources and technology companies to not-for-profit organisations and other small businesses. Moreover, my current client base stretches from Asia Pacific (incl. Australia), to Europe (incl. UK) and the US. All my clients speak English (even if as a second language) and are relatively senior communications professionals within their organisations.

Industry/Entity Type

Communications

Requirements
Nice to have
• The design/logo could include symbols and/or characters that double as imagery. For example: an upside down question mark (?) might look like a fishing line/hook and a flattened @ sign, might look like a pond...
Should not have
• The design should not use old-style serif fonts, but nor should it be "cartoony" in any way. No navy blue, grey or sombre corporate colours.

```html
<!DOCTYPE html>
<html lang="en">
<head>
<meta charset="utf-8">
<title>TallCedarRun stationery</title>
<link rel="stylesheet" href="https://fonts.googleapis.com/css2?family=Questrial&display=swap">
<style>
  :root {
    --ink: #1f2a5c;
    --accent: #f07a22;
    --tagline: #8c95a8;
    --rule: #bcbcc4;
    --paper: #ffffff;
    --edge: #d4d4d8;
    --shadow: rgba(0, 0, 0, 0.45);
  }
  * { margin: 0; padding: 0; box-sizing: border-box; }
  html, body { width: 1200px; height: 2172px; overflow: hidden; background: var(--paper); }
  body { position: relative; font-family: "Questrial", "Century Gothic", sans-serif; color: var(--ink); }
  .abs { position: absolute; white-space: nowrap; }

  .brand-name { color: var(--ink); letter-spacing: 0.02em; line-height: 1; }
  .brand-tag { color: var(--tagline); letter-spacing: 0.06em; line-height: 1; }
  .brand-dot { position: absolute; border-radius: 50%; background: var(--accent); }

  .hero-name { left: 62px; top: 150px; font-size: 100px; }
  .hero-tag { left: 557px; top: 266px; font-size: 44px; }
  .hero-dot { left: 772px; top: 92px; width: 52px; height: 52px; }

  .sheet { position: absolute; background: var(--paper); border: 1px solid var(--edge); box-shadow: 10px 10px 12px var(--shadow); }
  .letterhead { left: 58px; top: 345px; width: 975px; height: 1260px; }
  .card { top: 949px; width: 400px; height: 227px; }
  .card-front { left: 303px; }
  .card-back { left: 747px; }
  .comp-slip { left: 58px; top: 1651px; width: 1091px; height: 473px; }

  .rules { position: absolute; left: 0; top: 0; width: 1200px; height: 2172px; pointer-events: none; }
  .rules line { stroke: var(--rule); stroke-width: 1.6; }

  .copy { font-size: 17px; line-height: 24.5px; color: var(--ink); }
  .contact { font-size: 17px; line-height: 21px; }
  .card-details { font-size: 16.5px; line-height: 19px; letter-spacing: 0.08em; }
</style>
</head>
<body>
  <div class="abs brand-name hero-name">Tall Cedar Run</div>
  <span class="brand-dot hero-dot"></span>
  <div class="abs brand-tag hero-tag">Filler text for modo</div>

  <div class="sheet letterhead"></div>
  <div class="sheet comp-slip"></div>
  <div class="sheet card card-front"></div>
  <div class="sheet card card-back"></div>

  <svg class="rules" viewBox="0 0 1200 2172" aria-hidden="true">
    <line x1="415" y1="444" x2="845" y2="444"/>
    <line x1="845" y1="444" x2="845" y2="469"/>
    <line x1="173" y1="645" x2="845" y2="645"/>
    <line x1="173" y1="645" x2="173" y2="673"/>
    <line x1="845" y1="618" x2="845" y2="645"/>
    <line x1="173" y1="1336" x2="845" y2="1336"/>
    <line x1="173" y1="1309" x2="173" y2="1336"/>
    <line x1="845" y1="1336" x2="845" y2="1363"/>
    <line x1="173" y1="1536" x2="845" y2="1536"/>
    <line x1="845" y1="1509" x2="845" y2="1536"/>
    <line x1="329" y1="949" x2="329" y2="1149"/>
    <line x1="329" y1="1149" x2="673" y2="1149"/>
    <line x1="673" y1="1149" x2="673" y2="1176"/>
    <line x1="776" y1="1118" x2="776" y2="1149"/>
    <line x1="776" y1="1149" x2="1118" y2="1149"/>
    <line x1="1118" y1="1149" x2="1118" y2="1176"/>
    <line x1="120" y1="1651" x2="120" y2="2051"/>
    <line x1="120" y1="2051" x2="1082" y2="2051"/>
    <line x1="1082" y1="2051" x2="1082" y2="2124"/>
  </svg>

  <!-- letterhead -->
  <div class="abs brand-name" style="left:173px; top:421px; font-size:29px;">Tall Cedar Run</div>
  <span class="brand-dot" style="left:393px; top:416px; width:15px; height:15px;"></span>
  <div class="abs brand-tag" style="left:313px; top:456px; font-size:13px;">Filler text for modo</div>

  <div class="abs contact" style="left:845px; top:496px;">your name here<br>business address<br>somewherville, usa<br>5555</div>

  <div class="abs copy" style="left:173px; top:712px;">Dear sir,</div>
  <p class="abs copy" style="left:173px; top:750px;">Lorem ipsum dolor sit amet, consectetur adipisicing elit, sed do eiusmod<br>tempor incididunt ut labore et dolore magna aliqua. Ut enim ad minim veniam,<br>quis nostrudexercitation ullamco laboris nisi ut aliquip ex ea commodo<br>consequat. Duis aute irure dolor in reprehenderit in voluptate velit esse cillum<br>dolore eu fugiat nulla pariatur. Excepteur sint occaecat cupidatat non<br>proident, sunt in culpa qui officia deserunt mollit anim id est laborum.</p>

  <div class="abs copy" style="left:173px; top:1230px;">sincereley<br>your name here</div>

  <div class="abs contact" style="left:845px; top:1390px;">office phone<br>cell phone<br>email<br>fax number</div>

  <!-- business card, front -->
  <div class="abs brand-name" style="left:344px; top:1042px; font-size:29px;">Tall Cedar Run</div>
  <span class="brand-dot" style="left:564px; top:1034px; width:15px; height:15px;"></span>
  <div class="abs brand-tag" style="left:484px; top:1078px; font-size:13px;">Filler text for modo</div>

  <!-- business card, back -->
  <div class="abs card-details" style="left:776px; top:988px;">Your name here<br>Title<br><br>business phone<br>email<br>fax</div>

  <!-- compliment slip -->
  <div class="abs brand-name" style="left:134px; top:1746px; font-size:33px;">Tall Cedar Run</div>
  <span class="brand-dot" style="left:384px; top:1738px; width:17px; height:17px;"></span>
  <div class="abs brand-tag" style="left:278px; top:1788px; font-size:14px;">Filler text for modo</div>
</body>
</html>
```